Professional Website Design to match new logo for Medical Legal Company

We have rebranded our company and We want a professional but also dynamic web site design for a group of esteemed doctors that provide expert evaluation of an injured worker in a Workers Compensation case.
​
1. Our target market is both the attorneys who select our doctors and any doctors who would wish to join our group.

2. Notes for the Landing Page:
- We prefer a simpler, sleeker more modern look for the landing page.
- We want a simplified landing page with one image, three buttons highlighted in Content document.
- We want the main image to be black and white but it can be splashed with color.
-We think the landing page might be enhanced by add a dark blue or black as a primary color. Of course please feel free to try any color combination you think might work.
- We want "The Alder Circle" in large letters and "Stewards of a fair and prompt settlement" in small lettering. We don't want icons on the buttons.
- Do not want more than the one picture at top of landing page.
- We do not want any pictures that include faces. Please eliminate or replace. They will not be chosen.
- For the landing page, instead of a second set of photos please experiment with using medical symbols and legal symbols.
​
3. New Company Name: The Alder Circle
New logo is uploaded bronze and grey/silver will be colors although we are still tweaking the colors for more metallic feel. Want simple not busy.

4. The overall Web page design needs to have some website design effect (e,g image rollover, scrolling effect, hover effect etc).

5. Please follow the attached word document file for the page content of the 4 web pages. Do not mix it up.

Previous company website: www.clinjurisreview.example (we wish to convert some of the content from this website to the new brand). Competitor website that we like: www.rxboardly.example

Target Market(s)

Professional Elite. Attorneys and Doctors

Industry/Entity Type

Medical Legal

Coding

Coded - Design and coding required

Number of Pages Required

5+ page

Font styles to use
Other font styles liked:
• Helvetica or maybe font that matches logo. We are open

Colors

Designer to choose colors to be used in the design.

Requirements
Must have
• I can't locate on color scale but we want Bronze and Silver/Grey from logo. Additional colors can be added. Various shades of grey
Nice to have
• Black and white photos, simple elegant design
Should not have
• Images with faces of unknown people

```html
<!DOCTYPE html>
<html lang="en">
<head>
<meta charset="utf-8">
<title>The Alder Circle</title>
<link rel="stylesheet" href="https://fonts.googleapis.com/css2?family=Arimo:ital,wght@0,400;0,700;1,400&display=swap">
<style>
:root{
  --bronze:#8b3a22;
  --bronze-light:#a86b57;
  --ink:#1e1e1e;
  --charcoal:#2b2b2b;
  --grey:#6b6b6b;
  --grey-mid:#8a8a8a;
  --grey-soft:#c9c9c9;
  --grey-light:#e6e6e6;
  --white:#ffffff;
}
*{margin:0;padding:0;box-sizing:border-box}
html,body{width:1200px;height:4608px;overflow:hidden}
body{font-family:"Arimo",Helvetica,Arial,sans-serif;color:var(--ink);background:var(--white);position:relative}
section,header,footer{position:absolute;left:0;width:1200px}
.abs{position:absolute}
a{color:inherit;text-decoration:none}

/* header */
.site-header{top:0;height:95px;background:var(--charcoal);color:var(--white)}
.brand{left:111px;top:28px;font-size:28px;font-weight:700;letter-spacing:.5px}
.utility-nav{right:111px;top:18px;font-size:15px}
.main-nav{right:111px;top:56px;font-size:16px;display:flex;gap:19px}

/* hero: the single photograph */
.hero{top:95px;height:620px;background:linear-gradient(90deg,#f2f2f2 0%,#dcdcdc 38%,#8f8f8f 62%,#b8b8b8 82%,#e4e4e4 100%)}
.hero-title{left:111px;top:140px;font-size:50px;font-weight:700;line-height:62px}
.hero-title .accent{color:var(--bronze)}
.btn{display:flex;align-items:center;justify-content:center;border-radius:40px;font-weight:700;font-size:17px}
.btn-bronze{background:var(--bronze);color:var(--white)}
.hero .btn{left:111px;top:368px;width:332px;height:64px;font-size:16px}
.slider-dots{left:547px;top:551px;display:flex;gap:8px}
.slider-dots span{width:30px;height:4px;background:#9a9a9a}
.slider-dots span:first-child{background:var(--white)}

/* features */
.features{top:715px;height:313px}
.feature-title{font-size:24px;font-weight:700;line-height:30px}
.feature-text{font-size:15px;line-height:24px;color:var(--grey)}
.feature-link{font-size:17px;font-weight:700;color:var(--bronze)}
.divider{left:599px;top:62px;width:1px;height:165px;background:#cfcfcf}

/* welcome */
.welcome{top:1028px;height:783px;background:linear-gradient(90deg,#883620 0%,#8f4029 55%,#a86b57 100%);color:var(--white)}
.welcome h2{left:111px;top:172px;font-size:42px;line-height:53px;font-weight:700}
.welcome .intro{left:111px;top:360px;width:320px;font-size:17px;line-height:28px}
.btn-white{background:var(--white);color:var(--ink)}
.welcome .btn{left:111px;top:599px;width:170px;height:61px}
.standards{left:490px;top:76px;width:600px}
.standards h3{font-size:24px;font-weight:700;margin-bottom:18px}
.standards p{font-size:15px;line-height:25px;margin-bottom:22px}
.standards ul{list-style:none}
.standards li{font-size:15px;line-height:23px;padding-left:24px;position:relative;margin-bottom:23px}
.standards li svg{position:absolute;left:0;top:5px}

/* services */
.services{top:1811px;height:696px}
.section-title{width:1200px;text-align:center;font-size:40px;font-weight:700}
.services .section-title{top:84px}
.services .lede{left:220px;width:760px;top:160px;text-align:center;font-size:15px;line-height:26px;color:var(--grey)}
.card{top:288px;width:314px;height:322px;color:var(--white)}
.card-symbol{background:linear-gradient(160deg,#9c9c9c,#5a5a5a 70%,#3d3d3d)}
.card-symbol svg{position:absolute;left:122px;top:64px}
.card-symbol .card-label{position:absolute;bottom:34px;width:100%;text-align:center;font-size:24px;font-weight:700;line-height:29px}
.card-feature{background:linear-gradient(90deg,#6e6e6e 0 34px,var(--bronze) 34px)}
.card-feature .inner{position:absolute;left:60px;top:26px;width:240px}
.card-feature h4{font-size:24px;line-height:29px;margin-bottom:14px}
.card-feature p{font-size:15px;line-height:24px;margin-bottom:14px}
.card-feature .more{font-size:16px;font-weight:700}
.arrow{width:20px;height:30px}

/* careers */
.careers-band{top:2507px;height:515px;background:linear-gradient(90deg,#5e5e5e,#8a8a8a 50%,#5e5e5e)}
.tab{width:124px;height:124px;border-radius:50%;display:flex;flex-direction:column;align-items:center;justify-content:center;gap:10px;font-size:19px;font-weight:700;background:rgba(255,255,255,.25);color:var(--white)}
.tab.active{background:var(--white);color:var(--ink)}
.careers-card{top:2793px;left:111px;width:978px;height:372px;background:var(--white);box-shadow:0 10px 30px rgba(0,0,0,.12)}
.careers-symbol{left:0;top:0;width:429px;height:372px;background:linear-gradient(120deg,#b5b5b5,#6e6e6e 60%,#3a3a3a)}
.careers-symbol svg{position:absolute;left:150px;top:122px}
.careers-card h2{left:497px;top:62px;font-size:40px;font-weight:700}
.careers-card p{left:497px;top:130px;width:420px;font-size:15px;line-height:26px;color:var(--grey)}
.careers-card .btn{left:499px;top:263px;width:168px;height:59px}

/* testimonials */
.testimonials{top:3165px;height:467px}
.testimonials .section-title{top:96px}
.badge-client{left:111px;top:198px;width:140px;height:140px;border-radius:50%;background:linear-gradient(135deg,#b8765f,#8b3a22);z-index:2}
.badge-client svg{position:absolute;left:44px;top:44px}
.quote-badge{left:225px;top:198px;width:140px;height:140px;border-radius:50%;background:#6b6b6b;z-index:1}
.quote{left:425px;top:212px;width:670px;font-size:19px;line-height:32px;font-style:italic;color:#333}
.cite{left:425px;top:362px;font-size:21px;font-weight:700}

/* contact */
.contact{top:3632px;height:516px}
.contact-panel{left:0;top:0;width:474px;height:516px;background:linear-gradient(180deg,#8b3a22,#9a4a31)}
.contact-field{left:474px;top:0;width:726px;height:516px;background:linear-gradient(180deg,#bdbdbd,#808080 50%,#4a4a4a)}
.contact-field svg{position:absolute;left:303px;top:168px}
.contact h2{left:111px;top:82px;font-size:40px;font-weight:700;color:var(--white)}
.contact-item{left:111px;display:flex;gap:18px;color:var(--white);font-size:17px;line-height:29px}
.icon-ring{width:45px;height:45px;border:2px solid var(--white);border-radius:50%;display:flex;align-items:center;justify-content:center;flex:none}

/* footer */
.site-footer{top:4148px;height:376px}
.footer-brand{left:111px;top:124px;font-size:34px;font-weight:700;color:var(--grey)}
.footer-col h5{font-size:17px;font-weight:700;margin-bottom:18px}
.footer-links{list-style:none;font-size:15px;line-height:26px;color:var(--grey)}
.footer-note{font-size:15px;color:var(--grey);margin-bottom:22px}
.email-field{width:383px;height:52px;border:1px solid #cfcfcf;padding-left:18px;display:flex;align-items:center;font-size:15px;color:var(--grey)}
.site-footer .btn{width:122px;height:52px;margin-top:26px;margin-left:4px}
.bottom-bar{left:0;width:1200px;top:4524px;height:84px;background:var(--charcoal);color:var(--white)}
.copyright{left:111px;top:32px;font-size:15px}
.social{top:22px;width:40px;height:40px;border:2px solid var(--white);border-radius:50%}
</style>
</head>
<body>

<header class="site-header">
  <div class="abs brand">The Alder Circle</div>
  <div class="abs utility-nav">Newsletter &nbsp;|&nbsp; Member Login</div>
  <nav class="abs main-nav">
    <a>About</a><a>Services</a><a>Education Courses</a><a>Physicians</a><a>Career</a><a>Attorneys</a><a>Blog</a><a>Contact</a>
  </nav>
</header>

<section class="hero" role="img" aria-label="Black and white photo of two doctors reviewing a tablet">
  <h1 class="abs hero-title"><span class="accent">Stewards</span> of a<br>fair and prompt<br>settlement</h1>
  <a class="abs btn btn-bronze">SCHEDULE A QME APPOINTMENT</a>
  <div class="abs slider-dots"><span></span><span></span><span></span></div>
</section>

<section class="features">
  <svg class="abs" style="left:111px;top:60px" width="112" height="118" viewBox="0 0 112 118" fill="none" stroke-width="3">
    <circle cx="56" cy="34" r="22" stroke="#555"/>
    <path d="M6 116v-26c0-16 20-24 50-24s50 8 50 24v26" stroke="#555"/>
    <path d="M34 70v22a10 10 0 0 0 20 0M78 70v16" stroke="#8b3a22"/>
  </svg>
  <div class="abs feature-title" style="left:266px;top:62px">Get Assistance From A<br>Medical Expert</div>
  <div class="abs feature-text" style="left:266px;top:136px;width:300px">Medical-Legal Experts are here to help you in all the various specialties.</div>
  <div class="abs feature-link" style="left:266px;top:222px">REQUEST EXPERT HELP &nbsp;&gt;&gt;</div>
  <div class="abs divider"></div>
  <svg class="abs" style="left:667px;top:62px" width="110" height="112" viewBox="0 0 110 112" fill="none" stroke="#555" stroke-width="3">
    <rect x="2" y="22" width="106" height="70" rx="4"/>
    <path d="M40 92v14M70 92v14M30 108h50"/>
    <rect x="42" y="2" width="40" height="32" rx="4" stroke="#8b3a22"/>
    <path d="M56 10l12 8-12 8z" stroke="#8b3a22"/>
    <path d="M14 52h34M14 64h34M14 76h24M62 52h34M62 64h34M62 76h24"/>
  </svg>
  <div class="abs feature-title" style="left:806px;top:62px">Qme Report Writing<br>Courses &amp; More</div>
  <div class="abs feature-text" style="left:806px;top:136px;width:270px">We offer multiple online courses to become certified or get you up - to - speed for certification exams.</div>
  <div class="abs feature-link" style="left:806px;top:222px">REQUEST EXPERT HELP &nbsp;&gt;&gt;</div>
</section>

<section class="welcome">
  <h2 class="abs">WELCOME TO<br>THE ALDER<br>CIRCLE</h2>
  <p class="abs intro">The Alder Circle is a leader in Qualified Medical Evaluations and SIBTF cases in the State of California. Our doctors are dedicated facilitating settlements through rapid, objective and well researched Expert Medical Opinions .</p>
  <a class="abs btn btn-white">ABOUT US</a>
  <div class="abs standards">
    <h3>Highest Standard in Medical Reporting</h3>
    <p>The Alder Circle strives to uphold the Highest Standard in Medical Reporting. Following is a list to best describe what to expect when you receive QME Report from one of our Stewards:</p>
    <ul>
      <li><svg width="14" height="12" viewBox="0 0 14 12"><path d="M1 6l4 4 8-9" stroke="#fff" stroke-width="2.5" fill="none"/></svg><b>Timely:</b> Unless special circumstances exist, you can expect to receive the report well ahead of DWC imposed deadlines</li>
      <li><svg width="14" height="12" viewBox="0 0 14 12"><path d="M1 6l4 4 8-9" stroke="#fff" stroke-width="2.5" fill="none"/></svg><b>Clear, Concise and Readable:</b> So your valuable time is not wasted</li>
      <li><svg width="14" height="12" viewBox="0 0 14 12"><path d="M1 6l4 4 8-9" stroke="#fff" stroke-width="2.5" fill="none"/></svg><b>Impartial:</b> (all of our reports are reviewed by a 3rd party for Objectivity</li>
      <li><svg width="14" height="12" viewBox="0 0 14 12"><path d="M1 6l4 4 8-9" stroke="#fff" stroke-width="2.5" fill="none"/></svg><b>High Level Review</b> of Records by the Physician with Commentary</li>
      <li><svg width="14" height="12" viewBox="0 0 14 12"><path d="M1 6l4 4 8-9" stroke="#fff" stroke-width="2.5" fill="none"/></svg><b>Detailed and Comprehensive</b> Medical History</li>
      <li><svg width="14" height="12" viewBox="0 0 14 12"><path d="M1 6l4 4 8-9" stroke="#fff" stroke-width="2.5" fill="none"/></svg><b>No Conclusory Findings:</b> Thoroughly discussed conclusions for Apportionment, Causation and Impairment that are medical evidence based</li>
      <li><svg width="14" height="12" viewBox="0 0 14 12"><path d="M1 6l4 4 8-9" stroke="#fff" stroke-width="2.5" fill="none"/></svg><b>Comprehensive Analysis</b> of all injured body parts focused on the medical, not legal aspects of the case</li>
      <li><svg width="14" height="12" viewBox="0 0 14 12"><path d="M1 6l4 4 8-9" stroke="#fff" stroke-width="2.5" fill="none"/></svg><b>Answers to all questions</b> stated in the Cover Letter</li>
      <li><svg width="14" height="12" viewBox="0 0 14 12"><path d="M1 6l4 4 8-9" stroke="#fff" stroke-width="2.5" fill="none"/></svg><b>Future Medical Care</b> Section that is thoughtful and addresses both the short term and long term needs of the applicant</li>
    </ul>
  </div>
</section>

<section class="services">
  <h2 class="abs section-title">OUR SERVICES</h2>
  <p class="abs lede">We provide exceptional nationwide service of Medical-Legal Examinations (IME, QME &amp; AME), Peer Reviews, Record Reviews, Functional Capacity Evaluations (FCE), Expert Witness Testimony, and Subsequent Injuries Benefit Trust Fund (SIBTF) eligibility determinations</p>
  <svg class="abs arrow" style="left:51px;top:432px" viewBox="0 0 20 30"><path d="M16 2L4 15l12 13" stroke="#888" stroke-width="3" fill="none"/></svg>
  <div class="abs card card-symbol" style="left:111px">
    <svg width="70" height="70" viewBox="0 0 70 70"><path d="M25 2h20v23h23v20H45v23H25V45H2V25h23z" fill="none" stroke="#fff" stroke-width="3"/></svg>
    <div class="card-label">Expert Source<br>Methodology</div>
  </div>
  <div class="abs card card-feature" style="left:443px">
    <div class="inner">
      <h4>Extensive Medical Expert Network</h4>
      <p>With over 200 physician in our network, we are sure to have the right expert to have the right expert t meet your needs All of our physician are highly credentialed and experienced.</p>
      <div class="more">READ MORE &nbsp;&gt;&gt;</div>
    </div>
  </div>
  <div class="abs card card-symbol" style="left:774px">
    <svg width="70" height="70" viewBox="0 0 70 70" fill="none" stroke="#fff" stroke-width="3"><path d="M35 4v60M20 66h30M8 14h54"/><path d="M14 14L4 40h20zM56 14L46 40h20z"/></svg>
    <div class="card-label">Medical-Legal<br>Service</div>
  </div>
  <svg class="abs arrow" style="left:1129px;top:432px" viewBox="0 0 20 30"><path d="M4 2l12 13L4 28" stroke="#888" stroke-width="3" fill="none"/></svg>
</section>

<section class="careers-band">
  <div class="abs tab active" style="left:385px;top:93px">
    <svg width="32" height="28" viewBox="0 0 32 28"><rect x="1" y="7" width="30" height="20" rx="3" fill="#8b3a22"/><path d="M11 7V3h10v4" stroke="#8b3a22" stroke-width="3" fill="none"/></svg>Career</div>
  <div class="abs tab" style="left:537px;top:93px">
    <svg width="30" height="30" viewBox="0 0 30 30"><rect x="8" y="2" width="14" height="9" transform="rotate(45 15 6)" fill="#fff"/><path d="M12 14L3 27" stroke="#fff" stroke-width="4"/></svg>Attorneys</div>
  <div class="abs tab" style="left:689px;top:93px">
    <svg width="26" height="30" viewBox="0 0 26 30"><circle cx="13" cy="8" r="7" fill="#fff"/><path d="M0 30c0-9 5-13 13-13s13 4 13 13z" fill="#fff"/></svg>Applicants</div>
</section>

<div class="abs careers-card">
  <div class="abs careers-symbol">
    <svg width="128" height="128" viewBox="0 0 128 128" fill="none" stroke="#fff" stroke-width="4"><circle cx="64" cy="64" r="60" stroke-opacity=".5"/><path d="M54 30h20v24h24v20H74v24H54V74H30V54h24z"/></svg>
  </div>
  <h2 class="abs">CAREERS</h2>
  <p class="abs">Lorem ipsum dolor sit amet, consectetur adipiscing elit, sed do eiusmod tempor incididunt ut labore et dolore ma gna aliqua. Ut enim ad minim veniam, quis nostrud exerc itation ullamco laboris nisi ut aliquip ex.</p>
  <a class="abs btn btn-bronze">READ MORE</a>
</div>

<section class="testimonials">
  <h2 class="abs section-title">CLIENT TESTIMONIALS</h2>
  <svg class="abs arrow" style="left:51px;top:253px" viewBox="0 0 20 30"><path d="M16 2L4 15l12 13" stroke="#888" stroke-width="3" fill="none"/></svg>
  <div class="abs quote-badge">
    <svg class="abs" style="left:58px;top:46px" width="58" height="46" viewBox="0 0 58 46"><path d="M2 46V24C2 10 10 2 24 0v9c-7 2-10 6-10 13h10v24zM34 46V24C34 10 42 2 56 0v9c-7 2-10 6-10 13h10v24z" fill="#fff"/></svg>
  </div>
  <div class="abs badge-client">
    <svg width="52" height="52" viewBox="0 0 52 52" fill="none" stroke="#fff" stroke-width="3"><path d="M26 4v44M12 48h28M4 12h44"/><path d="M10 12L3 30h14zM42 12l-7 18h14z"/></svg>
  </div>
  <p class="abs quote">“ Nemo enim ipsam voluptatem quia voluptas sit aspernatur aut odit aut fgit, sed quia consequuntur magni dolores eos qui ratione voluptatem seq ui nes ciunt. Neque porro quisquam est, qui dolorem ipsum quia dolor sit amet, co nsectetur, adipisci velit, sed quia non numquam.”</p>
  <div class="abs cite">- Marisol</div>
  <svg class="abs arrow" style="left:1129px;top:253px" viewBox="0 0 20 30"><path d="M4 2l12 13L4 28" stroke="#888" stroke-width="3" fill="none"/></svg>
</section>

<section class="contact">
  <div class="abs contact-panel"></div>
  <div class="abs contact-field">
    <svg width="120" height="160" viewBox="0 0 120 160" fill="none" stroke="#fff" stroke-width="4" stroke-opacity=".8"><path d="M60 156S6 90 6 56a54 54 0 0 1 108 0c0 34-54 100-54 100z"/><circle cx="60" cy="56" r="20"/></svg>
  </div>
  <h2 class="abs">CONTACT US</h2>
  <div class="abs contact-item" style="top:180px">
    <span class="icon-ring"><svg width="16" height="22" viewBox="0 0 16 22"><path d="M8 21S1 12 1 8a7 7 0 0 1 14 0c0 4-7 13-7 13z" stroke="#fff" stroke-width="2" fill="none"/><circle cx="8" cy="8" r="2.5" fill="#fff"/></svg></span>
    <div>HEADQUARTERS<br>2210 Brightwater Ave.<br>6th Floor<br>Fernvale, CA 90411</div>
  </div>
  <div class="abs contact-item" style="top:323px;align-items:center">
    <span class="icon-ring"><svg width="20" height="20" viewBox="0 0 20 20"><path d="M4 1l4 4-2 3c1 3 3 5 6 6l3-2 4 4-3 3C8 19 1 12 1 4z" fill="#fff"/></svg></span>
    <div>Call toll free (800) 555-0142</div>
  </div>
  <div class="abs contact-item" style="top:381px;align-items:center">
    <span class="icon-ring"><svg width="20" height="20" viewBox="0 0 20 20"><rect x="2" y="6" width="16" height="12" rx="2" stroke="#fff" stroke-width="2" fill="none"/><rect x="6" y="1" width="8" height="6" stroke="#fff" stroke-width="2" fill="none"/></svg></span>
    <div>Fax (310) 555-0187</div>
  </div>
</section>

<footer class="site-footer">
  <div class="abs footer-brand">The Alder Circle</div>
  <div class="abs footer-col" style="left:501px;top:66px">
    <h5>Quick Links</h5>
    <ul class="footer-links">
      <li>Home</li><li>About</li><li>Services</li><li>Education Courses</li><li>Physicians</li><li>Career</li><li>Attorneys</li><li>Blog</li><li>Contact</li>
    </ul>
  </div>
  <div class="abs footer-col" style="left:706px;top:66px">
    <h5>Newsletter Sign Up</h5>
    <p class="footer-note">Enter your email address to get updates</p>
    <div class="email-field">Email Address</div>
    <a class="btn btn-bronze">SUBMIT</a>
  </div>
</footer>

<div class="abs bottom-bar">
  <div class="abs copyright">© 2024, The Alder Circle. All rights reserved.</div>
  <span class="abs social" style="left:946px"></span>
  <span class="abs social" style="left:996px"></span>
  <span class="abs social" style="left:1046px"></span>
</div>

</body>
</html>
```